movie poster for a bittersweet romantic drama

Hello everyone. Looking for a dynamic poster for feature film 'Mabel's Harbor' a romantic drama. It is a bittersweet love story so not rosey lovie dovie type.

300dpi

Please visit the link below for the poster image
https://www.filevault-example.net/s/k8p2r41xqz7mv5b/_Q7T4416.tif?dl=0

poster should have:
1. title of film : Mabel's Harbor
2. tagline of film:
Death knows no names
Love does not know race

3. A film by Lucinda P. Okwemba
4 Include the logo for 'Teruvo Films' attached below

poster size:
1. 8x10
2. thumnail
3. landscape with just film title
4. 27 by 41

Target Market(s)

15-55 men and mostly women

Industry/Entity Type

Film Production

Colors

Designer to choose colors to be used in the design.

Requirements
Must have
• Dynamic and vibrant
• it is a romantic drama so love on a serious note
Nice to have
• Play with romantic fonts but don't overdo it.
Should not have
• must not look like a romance novel

```html
<!DOCTYPE html>
<html lang="en">
<head>
<meta charset="utf-8">
<title>Mabel's Harbor — Poster</title>
<link rel="stylesheet" href="https://fonts.googleapis.com/css2?family=Kaushan+Script&family=Special+Elite&family=Cormorant+SC:wght@500;600&display=swap">
<style>
  :root {
    --paper: #fdfde4;
    --ink: #262a22;
    --ink-soft: #3a3f33;
    --tag-dark: #4f5a4a;
    --tag-green: #5e8c4c;
    --sky: #bfe3ec;
    --cloud: #f2f4f0;
    --hill-green: #5e8a6e;
    --hill-pink: #b79a92;
    --field-yellow: #e4e05a;
    --field-orange: #e6a27a;
    --grass: #3fae7c;
    --title-top: #3d4a2b;
    --title-mid: #7a8a2e;
    --title-low: #2f3a26;
  }
  * { margin: 0; padding: 0; box-sizing: border-box; }
  html, body {
    width: 900px; height: 1200px; overflow: hidden;
    background: var(--paper);
  }
  .poster {
    position: relative;
    width: 900px; height: 1200px;
    background: var(--paper);
    overflow: hidden;
  }
  .landscape {
    position: absolute;
    left: 58px; top: 68px;
    width: 768px; height: 722px;
  }
  .tagline {
    position: absolute;
    top: 806px;
    font-family: "Special Elite", "Courier New", monospace;
    font-size: 21px;
    letter-spacing: 0.3px;
  }
  .tagline--death { left: 204px; color: var(--tag-dark); }
  .tagline--love { left: 480px; color: var(--tag-green); }
  .title {
    position: absolute;
    left: 0; width: 900px;
    top: 818px;
    text-align: center;
    padding-left: 40px;
    font-family: "Kaushan Script", cursive;
    font-size: 128px;
    line-height: 1.2;
    white-space: nowrap;
    background: linear-gradient(180deg, var(--title-top) 0%, var(--title-low) 35%, var(--title-mid) 55%, var(--title-low) 80%);
    -webkit-background-clip: text;
    background-clip: text;
    color: transparent;
  }
  .credit-line {
    position: absolute;
    left: 0; width: 900px;
    top: 1006px;
    text-align: center;
    padding-left: 24px;
    font-family: "Cormorant SC", serif;
    font-weight: 600;
    font-size: 25px;
    letter-spacing: 2px;
    color: var(--ink);
  }
  .studio {
    position: absolute;
    left: 58px; top: 1126px;
    display: flex; align-items: center; gap: 6px;
    font-family: "Cormorant SC", serif;
    font-weight: 600;
    font-size: 17px;
    color: var(--ink-soft);
  }
  .studio__dot {
    width: 14px; height: 14px; border-radius: 50%;
    background: var(--ink-soft);
  }
  .credits {
    position: absolute;
    left: 0; width: 900px;
    top: 1130px;
    text-align: center;
    padding-left: 26px;
    font-family: "Cormorant SC", serif;
    font-weight: 500;
    font-size: 16px;
    line-height: 19px;
    color: var(--ink);
  }
</style>
</head>
<body>
<main class="poster">
  <svg class="landscape" viewBox="0 0 768 722" role="img" aria-label="Watercolour-edged photograph of a cloudy sky over rocky green hills and a yellow flower field, with a translucent heart shape">
    <defs>
      <linearGradient id="sceneFill" x1="0" y1="0" x2="0" y2="1">
        <stop offset="0" stop-color="var(--sky)"/>
        <stop offset="0.2" stop-color="var(--cloud)"/>
        <stop offset="0.45" stop-color="var(--cloud)"/>
        <stop offset="0.53" stop-color="var(--hill-pink)"/>
        <stop offset="0.66" stop-color="var(--hill-green)"/>
        <stop offset="0.8" stop-color="var(--field-yellow)"/>
        <stop offset="0.88" stop-color="var(--field-orange)"/>
        <stop offset="0.96" stop-color="var(--grass)"/>
        <stop offset="1" stop-color="var(--paper)"/>
      </linearGradient>
      <filter id="softEdge"><feGaussianBlur stdDeviation="10"/></filter>
    </defs>
    <path d="M80 40 Q200 0 330 20 Q480 -5 620 30 Q720 50 740 150 Q768 300 750 430 Q770 560 740 690 Q600 722 400 706 Q200 722 40 700 Q0 580 30 440 Q5 300 40 180 Q30 80 80 40 Z" fill="url(#sceneFill)" filter="url(#softEdge)"/>
    <path d="M384 175 C330 80 190 70 150 160 C110 250 180 330 260 400 L402 600 L560 400 C640 320 720 250 680 160 C640 70 480 70 420 160 Z" fill="#ffffff" fill-opacity="0.3"/>
  </svg>

  <p class="tagline tagline--death">Death knows no names</p>
  <p class="tagline tagline--love">Love does not know race</p>

  <h1 class="title">Mabel's Harbor</h1>

  <p class="credit-line">A film by Lucinda P. Okwemba</p>

  <div class="studio"><span class="studio__dot"></span><span>Teruvo Films</span></div>

  <div class="credits">
    <p>Credits Regie by Author Name Scenario by Author Name</p>
    <p>Music by: Author Name Sounds by: Author Name</p>
    <p>Actor I: Actor Name Actor I: Actor Name Actor I: Actor Name</p>
  </div>
</main>
</body>
</html>
```